An expert for Professional and Technical Evaluation of Painting Work Needs a New Letterhead Design

I own a mid-sized painting company and also work as an expert for professional and technical evaluation of painting work in the area of Zurich.

Please read the project description and the must-have-requirements carefully!

I attached 1 PDF which will help you create a new letterhead design:

THE NEW DESIGN DOESN'T NEED A LOGO! (Because it won't represent a company, it represents only a service)
Updates

Dear designers We had a discussion about the location/placement of the design and came to the conclusion that we only want the design to be in the header area of the A4-paper. We would be glad to receive some revised version of your designs. Thank you and kind regards!

Project Deadline Extended
Reason: Due to the fact that only 20% of the designer have understood the brief and submitted designs that have met the requirements we decided to extend the contest deadline.

Project Deadline Extended
Reason: A great deal of good designs were submitted in the last few days. A big thank you to all the participating designers for your good work. We need a few more days to discuss some changes with certain designers and to decide which design will win.

Target Market(s)

(Insurance) Companies, partly also private clients.

Industry/Entity Type

Painting

Colors

Designer to choose colors to be used in the design.

Requirements
Must have
• All information (text, phone numbers, ...) of the old design ("old_letterhead_design.pdf") has also to be in the new one. Additional to that there are a few changes:
The phone numbers "01 583 61 47" and "01 583 61 37" change to "044 583 61 47" and "044 583 61 37". And please mention also this email address: gutachten@valmorkeller.example .

- The design should only be in the header-area of the A4-paper. An the background color of the A4-paper will be white.

- The design should consist of two designs. One for the first page and a smaller version of the design for the following pages.

- THE NEW DESIGN DOESN'T NEED A LOGO! You can make a design with geometric forms, ...

- The new design should have a juridical look. It should only contain colors like brown, fawn, black, light green, ...... colors which look serious/reliable.
Nice to have
• Geometric Forms, Symbols or other design elements.

- It would also be nice to have some design elements which emphasize the kind of work we are offering.

```html
<!DOCTYPE html>
<html lang="de">
<head>
<meta charset="utf-8">
<title>Briefpapier Valmor Keller</title>
<link rel="stylesheet" href="https://fonts.googleapis.com/css2?family=Arimo:wght@400;700&display=swap">
<style>
  :root {
    --backdrop: #8f8f8f;
    --paper: #ffffff;
    --brown: #5a3e2b;
    --fawn: #b8926a;
    --ink: #2b2420;
    --ghost: #f3eee8;
  }
  * { box-sizing: border-box; margin: 0; padding: 0; }
  html, body { width: 1200px; height: 640px; overflow: hidden; }
  body {
    background: var(--backdrop);
    font-family: "Arimo", Arial, sans-serif;
    position: relative;
  }
  .sheet {
    position: absolute;
    top: 40px;
    width: 396px;
    height: 560px;
    background: var(--paper);
    box-shadow: 4px 4px 10px rgba(0,0,0,0.3);
    overflow: hidden;
  }
  .sheet--first { left: 150px; }
  .sheet--following { left: 654px; }

  .header-wave {
    position: absolute;
    left: 0; top: 0;
    width: 100%;
  }
  .sheet--first .header-wave { height: 20px; }
  .sheet--following .header-wave { height: 14px; }

  .brand {
    position: absolute;
    display: flex;
    align-items: center;
    gap: 6px;
    color: var(--brown);
    font-weight: 700;
  }
  .brand__mark { background: var(--fawn); }
  .sheet--first .brand { top: 28px; left: 26px; font-size: 14px; }
  .sheet--first .brand__mark { width: 12px; height: 12px; }
  .sheet--following .brand { top: 24px; left: 26px; font-size: 9px; gap: 4px; }
  .sheet--following .brand__mark { width: 8px; height: 8px; }

  .header-info {
    position: absolute;
    top: 28px;
    right: 22px;
    display: flex;
    gap: 5px;
    font-size: 5.6px;
    line-height: 7.4px;
    color: var(--ink);
  }
  .services { list-style: none; text-align: right; }
  .services li::after {
    content: "";
    display: inline-block;
    width: 3.4px; height: 3.4px;
    border-radius: 50%;
    background: var(--fawn);
    margin-left: 3px;
    vertical-align: middle;
  }
  .divider { width: 0.8px; background: var(--brown); }
  .contacts { list-style: none; }
  .contacts li { display: flex; align-items: center; gap: 3px; }
  .contacts svg { width: 5.5px; height: 5.5px; fill: var(--brown); flex: none; }

  .ghost-name {
    position: absolute;
    left: 0; right: 0;
    top: 255px;
    text-align: center;
    font-size: 46px;
    font-weight: 700;
    color: var(--ghost);
  }
</style>
</head>
<body>

<section class="sheet sheet--first" aria-label="Briefbogen erste Seite">
  <svg class="header-wave" viewBox="0 0 396 20" preserveAspectRatio="none" aria-hidden="true">
    <path fill="var(--brown)" d="M0 0 H396 V4 C260 5 150 8 0 14 Z"/>
    <path fill="var(--fawn)" d="M130 12 C220 9 320 7 396 7 V12 C310 12 220 13 130 12 Z"/>
  </svg>

  <div class="brand"><span class="brand__mark"></span>Valmor Keller</div>

  <div class="header-info">
    <ul class="services">
      <li>Gutachten</li>
      <li>Expertisen</li>
      <li>Devisierungen</li>
      <li>Farbberatungen</li>
      <li>Dekorative Gestaltungen</li>
    </ul>
    <span class="divider"></span>
    <ul class="contacts">
      <li><svg viewBox="0 0 10 10"><path d="M2 1h2l1 2.5-1.3 1a5 5 0 0 0 2.3 2.3l1-1.3L9.5 6.5v2A1 1 0 0 1 8.5 9.5 8 8 0 0 1 .5 1.5 1 1 0 0 1 2 1z"/></svg>044 583 61 47</li>
      <li><svg viewBox="0 0 10 10"><path d="M2.5 0.5h5v3h-5zM1 4h8v4.5H7.5v1h-5v-1H1z"/></svg>044 583 61 37</li>
      <li><svg viewBox="0 0 10 10"><path d="M0.5 2h9v6h-9zM1.2 2.6 5 5.6l3.8-3V3.4L5 6.4 1.2 3.4z"/></svg>gutachten@valmorkeller.example</li>
      <li><svg viewBox="0 0 10 10"><circle cx="5" cy="5" r="4.5"/></svg>eidg.dipl.Malermeister</li>
    </ul>
  </div>

  <div class="ghost-name" aria-hidden="true">Valmor Keller</div>
</section>

<section class="sheet sheet--following" aria-label="Briefbogen Folgeseite">
  <svg class="header-wave" viewBox="0 0 396 14" preserveAspectRatio="none" aria-hidden="true">
    <path fill="var(--brown)" d="M0 0 H396 V3 C260 4 150 6 0 10 Z"/>
    <path fill="var(--fawn)" d="M140 9 C230 7 320 5 396 5 V8.5 C310 8.5 220 9.5 140 9 Z"/>
  </svg>

  <div class="brand"><span class="brand__mark"></span>Valmor Keller</div>

  <div class="ghost-name" aria-hidden="true">Valmor Keller</div>
</section>

</body>
</html>
```